Luxury tennis village/academy - Webdesign

We want to develop a cutting edge website for a luxury tennis academy. Academy is based in Russia and includes all the necessary amenities for comfortable stay: apartments, spa, tennis courts, training facilities, etc.
We would like to see a clean, simple and modern design (with implementation of all the current trends in web design, although our project has to be distinct and unique).
Color scheme: we would like to see colors present in our logos and all the current associated with tennis. We are open to your ideas and creativity on this front.
The final design should communicate simplicity, be user friendly and convey premium feel.
We woud like to see unique ideas in the design, unconventional techniques, etc.
We don't want standard template design!
Updates
We want to mention that this Tennis Academy has a light focus on nature, as the new material we have uploaded illustrates.
Additional comment to everyone!
We couldn't upload this file to the system: it is too big.
Thank you everyone for your submissions!
Industry/Entity Type
Training
Requirements
Must have
- We would like to see the designs for the following pages:
Home Page:
- Slideshow
- Short description and all the standard stuff
About Us:
- Description with some images
Services:
- Simple description of all of the provided services and possibility to book all of them on the website
! Important ! Develop small system for booking of the days of stay and registration for the courses
Booking and registration !
News:
- Creative layout to display recent news of the academy
Coaches:
- Image and short description of our staff.
Club / Gallery:
- Images and descriptions of the amenities in the territory.
We want a unique display of images: not just lines and rows filled with images
- One idea: an interactive map that displays images and description on mouseover or click on the object on the map (but again, we are open to all your ideas)
Contacts:
- Contact form, contacts, etc.
Sport Store:
- Basic layout for the goods and services provided by the sports store located in the academy
Prices:
- Price lists and ranges with a button leading to registration and booking
For pages like About Us and Services, it would be enough to develop one unified layout for all of them.

```html
<!DOCTYPE html>
<html lang="en">
<head>
<meta charset="utf-8">
<title>Pinecourt – About Us</title>
<link rel="stylesheet" href="https://fonts.googleapis.com/css2?family=Roboto:wght@300;400;700&display=swap">
<style>
  :root {
    --page: #ffffff;
    --court-dark: #2c3a26;
    --court-mid: #4e6a3c;
    --clay: #a88a70;
    --overlay: rgba(22, 30, 20, 0.62);
    --text: #ffffff;
    --text-soft: rgba(255, 255, 255, 0.78);
    --rule: rgba(255, 255, 255, 0.35);
  }
  html, body {
    margin: 0;
    width: 1200px;
    height: 1000px;
    overflow: hidden;
    background: var(--page);
    font-family: "Roboto", Arial, sans-serif;
  }
  .stage {
    position: relative;
    width: 1200px;
    height: 1000px;
  }
  .hero-photo {
    position: absolute;
    left: 0; top: 200px;
    width: 1200px; height: 600px;
    background:
      linear-gradient(180deg, #3d5234 0%, #45603a 35%, #3a4d30 60%, #6f6650 78%, #b39478 88%, #a88a70 100%);
  }
  .panel {
    position: absolute;
    left: 0; top: 257px;
    width: 1200px; height: 456px;
    background: var(--overlay);
    border-top: 1px solid rgba(255,255,255,0.12);
    border-bottom: 1px solid rgba(255,255,255,0.12);
  }
  .brand {
    position: absolute;
    top: 226px; left: 0; width: 1200px;
    display: flex; justify-content: center; align-items: center; gap: 14px;
    color: var(--text);
    font-weight: 700;
    font-size: 52px;
    letter-spacing: 1px;
  }
  .brand-dot {
    width: 44px; height: 44px; border-radius: 50%;
    background: var(--text);
  }
  .main-nav {
    position: absolute;
    top: 328px; left: 0; width: 1200px;
    display: flex; justify-content: center; gap: 17px;
    font-weight: 300; font-size: 15px;
    color: var(--text-soft);
    text-transform: uppercase;
  }
  .nav-rule {
    position: absolute; top: 350px; left: 150px; width: 900px;
    height: 1px; background: rgba(255,255,255,0.12);
  }
  .section-title {
    position: absolute; left: 129px; top: 436px;
    margin: 0;
    font-weight: 300; font-size: 30px;
    color: var(--text-soft);
    letter-spacing: -0.5px;
  }
  .about-text {
    position: absolute; left: 361px; top: 437px;
    width: 452px; margin: 0;
    font-size: 14.5px; line-height: 19.3px;
    color: var(--text);
  }
  .gallery {
    position: absolute; left: 843px; top: 440px;
    display: grid; grid-template-columns: 100px 100px;
    column-gap: 12px; row-gap: 12px;
  }
  .thumb {
    width: 100px; height: 67px;
    box-sizing: border-box;
  }
  .thumb.is-active { border: 2px solid var(--text); }
  .thumb-park { background: linear-gradient(180deg, #5f8a4a, #8fa070); }
  .thumb-sky { background: linear-gradient(180deg, #6fb7e8 0%, #bcdff4 45%, #3f6a35 80%); }
  .thumb-meadow { background: linear-gradient(180deg, #4c7a3a, #7ea05a); }
  .thumb-grove { background: linear-gradient(180deg, #bfe0ef 0%, #5e8c44 55%, #8fb06a 100%); }
  .scroll-track {
    position: absolute; left: 1077px; top: 440px;
    width: 1px; height: 168px; background: var(--rule);
  }
  .scroll-thumb {
    position: absolute; left: 1075px; top: 440px;
    width: 5px; height: 38px; background: var(--text);
  }
  .footer-rule {
    position: absolute; left: 136px; top: 635px;
    width: 940px; height: 1px; background: var(--rule);
  }
  .contact-line {
    position: absolute; left: 0; top: 644px; width: 1200px;
    text-align: center; margin: 0;
    font-size: 13.5px; color: var(--text);
  }
</style>
</head>
<body>
<div class="stage">
  <div class="hero-photo" role="img" aria-label="Photo of a young tennis player on a clay court behind a green fence with trees"></div>
  <div class="panel"></div>

  <div class="brand"><span>Pinecourt</span><span class="brand-dot"></span></div>

  <nav class="main-nav">
    <span>Home</span><span>About us</span><span>Services</span><span>Booking and reservations</span>
    <span>News</span><span>Coaches</span><span>Club</span><span>Sport store</span><span>Prices</span><span>Contact</span>
  </nav>
  <div class="nav-rule"></div>

  <h1 class="section-title">ABOUT US</h1>
  <p class="about-text">Hoc vero, quod nimirum exigit legitimam kalendarii restitutionem, iamdiu a Romanis Pontificibus praedecessoribus nostris et saepius tentatum est; verum absolvi et ad exitum perduci ad hoc usque tempus non potuit, quod rationes emendandi kalendarii, quae a coelestium motuum peritis proponebantur, propter magnas et fere d nimirum exigit legitimam kalendarii restitutionem, iamdiu a Romanis Pontificibus praedecessoribus nostris et saepius tentatum est; verum absolvi et ad exitum</p>

  <div class="gallery">
    <div class="thumb thumb-park" role="img" aria-label="Park path among pine trees"></div>
    <div class="thumb thumb-sky" role="img" aria-label="Young pines under a blue sky"></div>
    <div class="thumb thumb-meadow is-active" role="img" aria-label="Meadow with pines and a horse"></div>
    <div class="thumb thumb-grove" role="img" aria-label="Pine grove with a horse"></div>
  </div>
  <div class="scroll-track"></div>
  <div class="scroll-thumb"></div>

  <div class="footer-rule"></div>
  <p class="contact-line">18, Linden Avenue, Northgate 104400. Phone: +7 800 5550142</p>
</div>
</body>
</html>
```